Brelford Fibers Holiday Card

Holiday card for our Textile company. Our corporate colors are orange and blue. See www.brelfordfibers-example.com for what we do. Basically we take flat man-made yarn and texture it to look and feel like wool or cotton. Our yarn is wound on an 11 inch cardboard tube (see website for pictures).

```html
<!DOCTYPE html>
<html lang="en">
<head>
<meta charset="utf-8">
<title>Brelford Fibers – Happy Holidays</title>
<link rel="stylesheet" href="https://fonts.googleapis.com/css2?family=Yellowtail&family=Oswald:wght@600&display=swap">
<style>
  :root {
    --knit-blue: #3d78c9;
    --knit-blue-deep: #2e62b2;
    --knit-blue-light: #4a86d4;
    --snow: #ffffff;
    --tag-orange: #c9611f;
    --tag-orange-deep: #9a4514;
    --tag-fold: #7c3610;
  }
  html, body {
    margin: 0;
    padding: 0;
    width: 1200px;
    height: 1200px;
    overflow: hidden;
    background: var(--knit-blue);
  }
  .card {
    position: relative;
    width: 1200px;
    height: 1200px;
    overflow: hidden;
  }
  .knit-background {
    position: absolute;
    inset: 0;
    background:
      repeating-linear-gradient(90deg, rgba(255,255,255,0.05) 0 14px, rgba(0,0,0,0.05) 14px 28px),
      radial-gradient(ellipse at 50% 45%, var(--knit-blue-light) 0%, var(--knit-blue) 55%, var(--knit-blue-deep) 100%);
  }
  .greeting {
    position: absolute;
    left: 0;
    top: 0;
    width: 1200px;
    height: 800px;
    margin: 0;
  }
  .greeting-line {
    font-family: "Yellowtail", "Brush Script MT", "Segoe Script", cursive;
    font-weight: 400;
    font-size: 270px;
    fill: var(--snow);
  }
  .brand-tag {
    position: absolute;
    left: 780px;
    top: 785px;
    width: 290px;
    height: 290px;
  }
  .brand-name {
    position: absolute;
    left: 800px;
    top: 860px;
    width: 225px;
    margin: 0;
    font-family: "Oswald", "Arial Narrow", sans-serif;
    font-weight: 600;
    font-size: 50px;
    line-height: 1.05;
    text-align: center;
    text-transform: uppercase;
    color: var(--snow);
  }
</style>
</head>
<body>
  <main class="card">
    <div class="knit-background" role="img" aria-label="Blue knitted wool texture"></div>

    <svg class="greeting" viewBox="0 0 1200 800" role="img" aria-label="Happy Holidays">
      <defs>
        <filter id="letterShadow" x="-5%" y="-5%" width="110%" height="120%">
          <feDropShadow dx="3" dy="5" stdDeviation="4" flood-color="#142e6e" flood-opacity="0.35"/>
        </filter>
      </defs>
      <g filter="url(#letterShadow)">
        <text class="greeting-line" x="295" y="420" textLength="715" lengthAdjust="spacingAndGlyphs">Happy</text>
        <text class="greeting-line" x="300" y="650" textLength="810" lengthAdjust="spacingAndGlyphs">Holidays</text>
      </g>
    </svg>

    <svg class="brand-tag" viewBox="0 0 290 290" aria-hidden="true">
      <defs>
        <linearGradient id="tagBody" x1="0" x2="1" y1="0" y2="0">
          <stop offset="0" stop-color="var(--tag-orange-deep)"/>
          <stop offset="0.25" stop-color="var(--tag-orange)"/>
          <stop offset="0.8" stop-color="var(--tag-orange)"/>
          <stop offset="1" stop-color="var(--tag-orange-deep)"/>
        </linearGradient>
      </defs>
      <path d="M20 30 Q130 15 245 25 L245 255 Q130 245 20 265 Z" fill="url(#tagBody)"/>
      <path d="M245 25 L275 10 L275 250 L245 255 Z" fill="var(--tag-fold)"/>
      <line x1="262" y1="22" x2="262" y2="245" stroke="var(--snow)" stroke-width="2.5" stroke-dasharray="7 6"/>
    </svg>
    <p class="brand-name">Brelford Fibers</p>
  </main>
</body>
</html>
```